Glidewell Depot logo

Glidewell Depot is owned and operated by industry professionals with years of direct experience in providing customers with the right equipment to suit their needs. Our specialty lies within dealing in the Halvern Medical range of products. Our product range is suited to both the new user and for those that know what they want, a full line of products ranging from ultra-light wheelchairs, wheelchairs for sport and recreation and paediatric or just everyday use.

Industry/Entity Type

Recreation

Contact Information for Business Card

name, title, landline,fax,mobile,email,web address,physical address,logo,possibly a wheelchair pic

Requirements
Must have
• logo - uploaded
Nice to have
• colour scheme consistent with
www.glidewelldepot.com.au

```html
<!DOCTYPE html>
<html lang="en">
<head>
<meta charset="utf-8">
<title>Glidewell Depot – Business Card</title>
<link href="https://fonts.googleapis.com/css2?family=Cabin:wght@400;500;600;700&display=swap" rel="stylesheet">
<style>
  :root {
    --page-bg: #e4e5e8;
    --card-white: #ffffff;
    --brand-blue-deep: #1d5597;
    --brand-blue: #2f74bb;
    --brand-blue-light: #5b9ad6;
    --logo-pale: #cfdcec;
    --accent-purple: #6a2a7c;
    --accent-cyan: #2a9ed6;
    --ink: #3a3a3a;
    --photo-light: #e9eaec;
    --photo-dark: #8d9096;
  }
  * { box-sizing: border-box; margin: 0; padding: 0; }
  html, body { width: 1200px; height: 900px; overflow: hidden; }
  body {
    background: var(--page-bg);
    font-family: "Cabin", "Gill Sans", sans-serif;
    position: relative;
  }
  .card {
    position: absolute;
    left: 280px;
    width: 640px;
    height: 366px;
    border-radius: 4px;
    box-shadow: 0 8px 24px rgba(0,0,0,.18);
    overflow: hidden;
  }

  /* Back of card */
  .card-back {
    top: 60px;
    background: radial-gradient(ellipse at 50% 42%, var(--brand-blue-light) 0%, var(--brand-blue) 40%, var(--brand-blue-deep) 100%);
    color: var(--logo-pale);
  }
  .back-logo {
    position: absolute;
    top: 120px;
    left: 0; right: 0;
    display: flex;
    justify-content: center;
    align-items: center;
    gap: 18px;
  }
  .back-logo-dot {
    width: 38px; height: 38px;
    border-radius: 50%;
    background: var(--logo-pale);
  }
  .back-logo-name {
    font-size: 54px;
    font-weight: 600;
    color: var(--logo-pale);
    letter-spacing: .5px;
  }
  .back-tagline {
    position: absolute;
    bottom: 64px;
    left: 0; right: 0;
    text-align: center;
    color: #ffffff;
    font-size: 17px;
    font-weight: 600;
    letter-spacing: 2px;
  }

  /* Front of card */
  .card-front {
    top: 474px;
    background: var(--card-white);
  }
  .front-logo {
    position: absolute;
    top: 30px;
    right: 36px;
    font-size: 52px;
    font-weight: 700;
    color: var(--accent-purple);
  }
  .front-services {
    position: absolute;
    top: 40px;
    left: 36px;
    font-size: 13px;
    color: var(--accent-cyan);
  }
  .holder {
    position: absolute;
    top: 100px;
    left: 36px;
    color: var(--accent-purple);
  }
  .holder-name { font-size: 26px; font-weight: 500; }
  .holder-title { font-size: 18px; margin-top: 2px; }
  .contact-list {
    position: absolute;
    top: 180px;
    left: 36px;
    list-style: none;
    font-size: 15px;
    line-height: 1.45;
    color: var(--ink);
  }
  .contact-label {
    display: inline-block;
    width: 22px;
    color: var(--accent-cyan);
  }
  .contact-address { margin-top: 4px; }
  .product-photo {
    position: absolute;
    right: 40px;
    bottom: 30px;
    width: 230px;
    height: 180px;
    border-radius: 6px;
    background: radial-gradient(ellipse at 50% 50%, var(--photo-light) 0%, #c4c6ca 60%, var(--photo-dark) 100%);
  }
</style>
</head>
<body>

  <section class="card card-back">
    <div class="back-logo">
      <span class="back-logo-dot"></span>
      <span class="back-logo-name">Glidewell Depot</span>
    </div>
    <p class="back-tagline">SERVICE - KNOWLEDGE - INNOVATION</p>
  </section>

  <section class="card card-front">
    <p class="front-services">Sales, Service and Repairs</p>
    <h1 class="front-logo">Glidewell Depot</h1>

    <div class="holder">
      <p class="holder-name">Marcus Trevell</p>
      <p class="holder-title">managing director</p>
    </div>

    <ul class="contact-list">
      <li><span class="contact-label">p:</span>02 9555 0142</li>
      <li><span class="contact-label">f:</span>02 9555 0143</li>
      <li><span class="contact-label">m:</span>0412 555 876</li>
      <li><span class="contact-label">e:</span>info@glidewelldepot.com.au</li>
      <li><span class="contact-label">w:</span>www.glidewelldepot.com.au</li>
      <li class="contact-address">48 Harbour Lane Brookvale, NSW 2100</li>
    </ul>

    <div class="product-photo" role="img" aria-label="Photo of an ultra-light manual wheelchair"></div>
  </section>

</body>
</html>
```